A layout of a webpage for oil trade platform

I would like to have a desgin of one page webpage (with section scrollling dowin) that woulf present the new product i.e. oil trade platform for wholesale buyers and sellers.
Layout should consist of the sections similar to the given at: https://klinika.pewnywybor.pl/system-zarzadzania-wizytami
However oil industy require more colors and more photo stories than here for doctor.
I. I woul imagine at first below menu a slider with brueg information about the product and its advantages with "more" button next to the prict screen of our platform on different displays (PC and mobile).
II. Bellow the slider I would imagine icons correspoing to the advantages of that plaftorm:
1. Purchase/sale process automation 24/7
2. Access to the best deals
3. Electronic offerings and orderings
4. Transaction status monitoring
5. Data and transaction security
II A) (optional):
In near future we would like to prepare a short video presenation. Hence please prepare a place to display that element here.
At the moment alternatvily please prepare a How it works section that would explan the platform operating process
III. Next secion is about benefits for Oil Purchaser
It can be done either by icons of by text and corresponding grahip for while section.
Benefits:
- Access to cheaper oil
- Convenience of online orders
- Possibility to compare prices on the market
- Transaction history
- Order status monitoring
- Seccurity and transparency of purchase
IV. Next seciont is about benefits for Oil Seller
Benefits:
- New sale channel
- Attracting new clients
- More oil sold
- Transaction security
- Possibility to integrate with distribution infrastructure and logistits for more efficient automation.
V. Contact form
VI. Footer
I would need a layout that that will correspond to the very dynamic logo but I would expect also a clean form, smoth and modern. It has to be proffessional layout with more corporate character.
It can use a paralax features if needed.

```html
<!DOCTYPE html>
<html lang="en">
<head>
<meta charset="utf-8">
<title>Oilvanta – Oil Trading Platform</title>
<link rel="stylesheet" href="https://fonts.googleapis.com/css2?family=Open+Sans:wght@300;400;600&family=Roboto:wght@300;400;500&display=swap">
<style>
:root{
  --orange:#f2622a;
  --orange-btn:#fb8a2e;
  --blue:#27aacd;
  --green:#45b35a;
  --ink:#333;
  --text:#555;
  --muted:#888;
  --line:#e6e6e6;
  --soft:#f6f6f6;
  --white:#fff;
}
*{box-sizing:border-box;margin:0;padding:0}
html,body{width:1200px;height:2808px;overflow:hidden}
body{position:relative;background:var(--white);font-family:"Open Sans",sans-serif;color:var(--text)}
.abs{position:absolute}
a{color:inherit;text-decoration:none}

/* hero */
.hero{left:0;top:0;width:1200px;height:539px;background:var(--orange);overflow:hidden}
.brand{left:88px;top:22px;display:flex;align-items:center;gap:10px;color:var(--white);font-family:"Roboto",sans-serif;font-weight:500;font-size:21px;letter-spacing:.5px}
.brand-dot{width:22px;height:22px;border-radius:50%;background:var(--white)}
.nav{right:135px;top:36px;display:flex;gap:32px;font-family:"Roboto",sans-serif;font-size:13.5px;color:var(--white)}
.hero-title{left:88px;top:152px;font-family:"Roboto",sans-serif;font-weight:400;font-size:33px;line-height:38px;color:var(--white)}
.hero-sub{left:88px;top:242px;font-family:"Roboto",sans-serif;font-size:17px;color:var(--white)}
.hero-text{left:88px;top:283px;width:360px;font-size:13px;line-height:23px;color:var(--white)}
.btn{display:flex;align-items:center;justify-content:center;gap:10px;background:var(--orange-btn);color:var(--white);border-radius:22px;font-family:"Roboto",sans-serif;font-size:12px;letter-spacing:.5px;box-shadow:0 8px 18px rgba(0,0,0,.15)}
.hero-btn{left:88px;top:371px;width:148px;height:43px}
.mockup{left:470px;top:110px;width:730px;height:360px;border-radius:6px 0 0 6px;background:linear-gradient(135deg,rgba(255,255,255,.35),rgba(255,255,255,.12))}

/* advantages */
.advantages{left:0;top:539px;width:1200px;height:300px;background:var(--soft)}
.adv{width:200px;text-align:center;top:96px}
.adv-icon{width:72px;height:72px;border-radius:50%;background:var(--white);margin:0 auto;display:flex;align-items:center;justify-content:center;position:relative;box-shadow:0 2px 6px rgba(0,0,0,.04)}
.adv-num{position:absolute;left:-2px;top:2px;width:18px;height:18px;border-radius:50%;background:#f0d6c8;color:var(--white);font-size:10px;line-height:18px}
.adv-num.on{background:var(--orange)}
.adv-label{margin-top:28px;font-size:12.5px;line-height:22px;color:var(--text)}
.dots{top:130px;height:0;border-top:2px dotted #d4d4d4;width:130px}

/* how it works */
.how-photo{left:0;top:921px;width:599px;height:322px;background:linear-gradient(135deg,#2f5d52,#b9c7c4 55%,#d9d2c6)}
.how-band{left:0;top:1243px;width:511px;height:69px;background:var(--green);color:var(--white);font-size:12px;letter-spacing:.5px;padding:28px 0 0 93px}
.play{left:408px;top:1211px;width:64px;height:64px;border-radius:50%;background:var(--white);display:flex;align-items:center;justify-content:center;box-shadow:0 4px 12px rgba(0,0,0,.15)}
.h2{font-family:"Open Sans",sans-serif;font-weight:400;font-size:27px;color:var(--ink)}
.rule{width:30px;height:2px;background:var(--orange);margin-top:10px}
.how-head{left:670px;top:974px}
.how-text{left:670px;top:1040px;width:398px;font-size:13px;line-height:24.5px}
.how-text p+p{margin-top:12px}

/* purchaser */
.buy-head{left:0;top:1374px;width:1200px;text-align:center}
.buy-head .rule{margin:10px auto 0}
.cards{left:88px;top:1440px;display:flex;gap:2px}
.card{width:169px;height:157px;border:1px solid var(--line);text-align:center;padding-top:36px}
.card-label{margin-top:12px;font-size:12.5px;line-height:19px;color:var(--text)}

/* seller */
.sell-head{left:88px;top:1719px}
.sell-item{display:flex;align-items:center;gap:12px;font-size:12.5px;color:var(--text)}
.sell-photo{left:599px;top:1659px;width:601px;height:383px;background:linear-gradient(135deg,#c9b8a2,#7d8a8f 50%,#3f4a4f)}

/* contact */
.contact-band{left:0;top:2108px;width:1200px;height:299px;background:var(--blue)}
.contact-head{left:0;top:2156px;width:1200px;text-align:center;color:var(--white)}
.contact-head .h2{color:var(--white)}
.contact-head .rule{margin:8px auto 0;background:var(--white)}
.footer-bg{left:0;top:2407px;width:1200px;height:401px;background:var(--soft)}
.form{left:88px;top:2229px;width:1024px;height:321px;background:var(--white);box-shadow:0 2px 10px rgba(0,0,0,.06)}
.field{position:absolute}
.field label{display:block;font-size:12px;color:var(--ink);font-weight:600}
.field .input{margin-top:10px;padding-bottom:12px;border-bottom:1px solid var(--line);font-size:13px;color:#aaa}
.send{left:512px;top:2477px;width:103px;height:43px}

/* footer */
.f-head{font-size:17px;color:var(--ink)}
.f-head .rule{margin-top:8px;width:26px}
.f-text{font-size:11.5px;line-height:22px;color:var(--text)}
.f-links li{list-style:none;font-size:11.5px;line-height:22px}
.f-links li::before{content:"›";margin-right:6px;color:var(--muted)}
.f-input{border-bottom:1px solid var(--line);font-size:12px;color:#aaa;padding-bottom:10px;width:310px}
.f-btn{width:45px;height:26px;border-radius:13px;background:var(--orange-btn);display:flex;align-items:center;justify-content:center}
.f-divider{left:88px;top:2757px;width:1024px;height:1px;background:var(--line)}
.copy{left:88px;top:2776px;font-size:11px;color:var(--ink)}
.to-top{left:1136px;top:2741px;width:38px;height:38px;border-radius:50%;background:var(--white);box-shadow:0 2px 8px rgba(0,0,0,.1);display:flex;align-items:center;justify-content:center}
svg{display:block}
.ic{stroke:#666;fill:none;stroke-width:1.6;stroke-linecap:round;stroke-linejoin:round}
.ic .acc{stroke:var(--orange)}
</style>
</head>
<body>

<!-- Hero -->
<section class="abs hero">
  <div class="abs brand"><span class="brand-dot"></span>Oilvanta</div>
  <nav class="abs nav"><a>Overview</a><a>Advantages</a><a>How It Works</a><a>Benefits</a><a>Contact</a></nav>
  <h1 class="abs hero-title">Get the perfect<br>Oil Trading Platform</h1>
  <p class="abs hero-sub">Quisque rutrum - Aenean imperdiet - Etiam ultricies</p>
  <p class="abs hero-text">Quisque rutrum aenean imperdiet etiam ultricies nisi vel augue curabitur ullamcorper ultricies nisi nam eget dui. Etiam rhoncus maecenas.</p>
  <a class="abs btn hero-btn">LEARN MORE
    <svg width="14" height="10" viewBox="0 0 14 10"><path d="M1 5h11M8 1l4 4-4 4" stroke="#fff" fill="none" stroke-width="1.4"/></svg></a>
  <div class="abs mockup" role="img" aria-label="Platform dashboard shown on a laptop and a mobile phone"></div>
</section>

<!-- Advantages -->
<section class="abs advantages">
  <div class="abs dots" style="left:235px"></div>
  <div class="abs dots" style="left:452px"></div>
  <div class="abs dots" style="left:665px"></div>
  <div class="abs dots" style="left:886px"></div>

  <div class="abs adv" style="left:82px">
    <div class="adv-icon"><span class="adv-num">1</span>
      <svg class="ic" width="38" height="38" viewBox="0 0 38 38"><path d="M31 12a14 14 0 1 0 2 10"/><path class="acc" d="M31 5v7h-7"/><text x="19" y="23" font-size="9" text-anchor="middle" fill="#f2622a" stroke="none" font-family="Roboto,sans-serif">24/7</text></svg></div>
    <p class="adv-label">Purchase/sale process<br>automation 24/7</p>
  </div>
  <div class="abs adv" style="left:299px">
    <div class="adv-icon"><span class="adv-num">2</span>
      <svg class="ic" width="34" height="34" viewBox="0 0 34 34"><rect x="5" y="7" width="22" height="22"/><path class="acc" d="M11 17l5 5 13-15"/></svg></div>
    <p class="adv-label">Access to the best deals</p>
  </div>
  <div class="abs adv" style="left:512px">
    <div class="adv-icon"><span class="adv-num on">3</span>
      <svg class="ic" width="34" height="38" viewBox="0 0 34 38"><rect x="10" y="4" width="14" height="24" rx="2"/><path class="acc" d="M6 10c-2 3-2 7 0 10M28 10c2 3 2 7 0 10"/><path d="M20 24v10l3-3 3 5"/></svg></div>
    <p class="adv-label">Electronic offerings<br>and orderings</p>
  </div>
  <div class="abs adv" style="left:733px">
    <div class="adv-icon"><span class="adv-num">4</span>
      <svg class="ic" width="36" height="36" viewBox="0 0 36 36"><path d="M6 18a12 12 0 0 1 21-8M30 18a12 12 0 0 1-21 8"/><path d="M27 4v6h-6M9 32v-6h6"/><path class="acc" d="M18 12v12M15 15h5a2 2 0 0 1 0 4h-4a2 2 0 0 0 0 4h5"/></svg></div>
    <p class="adv-label">Transaction status<br>monitoring</p>
  </div>
  <div class="abs adv" style="left:954px">
    <div class="adv-icon"><span class="adv-num">5</span>
      <svg class="ic" width="34" height="34" viewBox="0 0 34 34"><path d="M4 9h9l3 3h14v16H4z"/><rect class="acc" x="13" y="18" width="9" height="7"/><path class="acc" d="M15 18v-3a2.5 2.5 0 0 1 5 0v3"/></svg></div>
    <p class="adv-label">Data and transaction<br>security</p>
  </div>
</section>

<!-- How it works -->
<section>
  <div class="abs how-photo" role="img" aria-label="Woman working on a laptop in a bright office"></div>
  <div class="abs how-band">MAECENAS NEC ODIO ET ANT TINIDT TEMUS DONE.</div>
  <div class="abs play"><svg width="20" height="22" viewBox="0 0 20 22"><path d="M3 2l15 9-15 9z" fill="none" stroke="#f2622a" stroke-width="2" stroke-linejoin="round"/></svg></div>
  <div class="abs how-head"><h2 class="h2">How it works</h2><div class="rule"></div></div>
  <div class="abs how-text">
    <p>Aenean vulputate eleifend tellus aenean leo ligula porttitor eu consequat vitae eleifend ac enim. Aliquam lorem ante dapibus in viverra quis feugiat a tellus phasellus viverra nulla ut metus varius laoreet quisque rutrum aenean imperdiet etiam ultricies nisi vel augue.</p>
    <p>Lorem ante dapibus in viverra quis feugiat a tellus phasellus viverra nulla ut metus varius laoreet.</p>
  </div>
</section>

<!-- Benefits for purchaser -->
<section>
  <div class="abs buy-head"><h2 class="h2">Benefits for Oil Purchaser</h2><div class="rule"></div></div>
  <div class="abs cards">
    <div class="card"><svg class="ic" width="36" height="36" viewBox="0 0 36 36" style="margin:0 auto"><circle cx="18" cy="9" r="5"/><path d="M8 30v-6a10 10 0 0 1 20 0v6"/><path class="acc" d="M4 26h10l4 3h12"/></svg><p class="card-label">Access to<br>cheaper oil</p></div>
    <div class="card"><svg class="ic" width="36" height="36" viewBox="0 0 36 36" style="margin:0 auto"><circle cx="18" cy="14" r="10"/><path d="M8 14h20M18 4c-4 5-4 15 0 20M18 4c4 5 4 15 0 20"/><path class="acc" d="M18 26v7M14 29l4 4 4-4"/></svg><p class="card-label">Convenience of<br>online orders</p></div>
    <div class="card"><svg class="ic" width="36" height="36" viewBox="0 0 36 36" style="margin:0 auto"><path d="M4 11h8l12 14h8M4 25h8l4-5M20 16l4-5h8"/><path class="acc" d="M28 7l4 4-4 4M28 21l4 4-4 4"/></svg><p class="card-label">Compare prices<br>on the market</p></div>
    <div class="card"><svg class="ic" width="36" height="36" viewBox="0 0 36 36" style="margin:0 auto"><rect x="8" y="6" width="20" height="26"/><path class="acc" d="M14 12l6 6M20 18l3-2"/></svg><p class="card-label">Transaction<br>history</p></div>
    <div class="card"><svg class="ic" width="36" height="36" viewBox="0 0 36 36" style="margin:0 auto"><rect x="4" y="6" width="28" height="18"/><path d="M14 30h8M18 24v6"/><path class="acc" d="M13 16l4 3 6-7"/></svg><p class="card-label">Order status<br>monitoring</p></div>
    <div class="card" style="padding-top:26px"><svg class="ic" width="36" height="36" viewBox="0 0 36 36" style="margin:0 auto"><path d="M18 4l12 4v9c0 8-6 13-12 15-6-2-12-7-12-15V8z"/><path class="acc" d="M12 18l5 5 8-9"/></svg><p class="card-label">Security &amp;<br>transparency<br>of purchase</p></div>
  </div>
</section>

<!-- Benefits for seller -->
<section>
  <div class="abs sell-head"><h2 class="h2">Benefits for Oil Seller</h2><div class="rule"></div></div>
  <div class="abs sell-item" style="left:88px;top:1794px"><svg class="ic" width="30" height="30" viewBox="0 0 30 30"><path d="M4 16L16 4h10v10L14 26z"/><circle class="acc" cx="21" cy="9" r="2"/></svg>New sale channel</div>
  <div class="abs sell-item" style="left:266px;top:1794px"><svg class="ic" width="30" height="30" viewBox="0 0 30 30"><circle cx="15" cy="8" r="5"/><path d="M6 27v-5a9 9 0 0 1 18 0v5"/><path class="acc" d="M15 15v6"/></svg>Attracting new clients</div>
  <div class="abs sell-item" style="left:88px;top:1868px"><svg class="ic" width="30" height="30" viewBox="0 0 30 30"><path d="M8 4h11l5 5v17H8z"/><path class="acc" d="M12 15h8M12 19h8M12 23h5"/></svg>More oil sold</div>
  <div class="abs sell-item" style="left:266px;top:1868px"><svg class="ic" width="30" height="30" viewBox="0 0 30 30"><path d="M15 3l10 3v8c0 7-5 11-10 13-5-2-10-6-10-13V6z"/><path class="acc" d="M10 15l4 4 6-7"/></svg>Transaction security</div>
  <div class="abs sell-item" style="left:88px;top:1936px;align-items:flex-start"><svg class="ic" width="30" height="30" viewBox="0 0 30 30"><path class="acc" d="M12 18l-4 4a4 4 0 0 1-6-6l4-4"/><path d="M18 12l4-4a4 4 0 0 1 6 6l-4 4M11 19l8-8"/></svg><span style="line-height:24px;width:360px">Possibility to integrate with distribution infrastructure and logistits for more efficient automation.</span></div>
  <div class="abs sell-photo" role="img" aria-label="Team of colleagues smiling around a laptop at a shared desk"></div>
</section>

<!-- Contact -->
<section>
  <div class="abs contact-band"></div>
  <div class="abs footer-bg"></div>
  <div class="abs contact-head"><h2 class="h2">Contact us</h2><div class="rule"></div></div>
  <form class="abs form">
    <div class="field" style="left:44px;top:44px;width:460px"><label>Name:</label><div class="input">Enter your full name here...</div></div>
    <div class="field" style="left:543px;top:44px;width:437px"><label>Email address:</label><div class="input">Enter your email address...</div></div>
    <div class="field" style="left:44px;top:124px;width:936px"><label>Message:</label><div class="input" style="height:86px">Enter your message here...</div></div>
  </form>
  <a class="abs btn send">SEND
    <svg width="12" height="10" viewBox="0 0 12 10"><path d="M1 5h9M7 1l4 4-4 4" stroke="#fff" fill="none" stroke-width="1.4"/></svg></a>
</section>

<!-- Footer -->
<footer>
  <div class="abs" style="left:88px;top:2595px;width:420px">
    <h3 class="f-head" style="font-weight:400">About<div class="rule"></div></h3>
    <p class="f-text" style="margin-top:14px">Nullam dictum felis eu pede mollis pretium integer tincidunt cras dapibus vivamus elementum semper nisi aenean vulputate eleifend tellus aenean leo ligula porttitor eu consequat vitae eleifend ac.</p>
  </div>
  <div class="abs" style="left:580px;top:2595px">
    <h3 class="f-head" style="font-weight:400">Useful Links<div class="rule"></div></h3>
    <ul class="f-links" style="margin-top:14px"><li>Home</li><li>Privacy Policy</li><li>Terms &amp; Conditions</li></ul>
  </div>
  <div class="abs" style="left:794px;top:2595px">
    <h3 class="f-head" style="font-weight:400">Newsletter<div class="rule"></div></h3>
    <div class="f-input" style="margin-top:20px">Enter your email address...</div>
    <div class="f-btn" style="margin-top:10px"><svg width="12" height="12" viewBox="0 0 12 12"><path d="M1 6l10-5-4 10-1-4z" fill="#fff"/></svg></div>
  </div>
  <div class="abs f-divider"></div>
  <p class="abs copy">© 2017. All Rights Reserved.</p>
  <div class="abs to-top"><svg width="10" height="12" viewBox="0 0 10 12"><path d="M5 11V1M1 5l4-4 4 4" stroke="#333" fill="none" stroke-width="1.3"/></svg></div>
</footer>

</body>
</html>
```